Business card design needed

I have started a new business called Marlow Auto Electrical, although the words Marlow Auto Electrical will be used on signage and documents I actually want to market the business as MAE. The services I offer are Mobile Auto Electrical, Automotive Air Conditioning and Test And Tag. My business will be targetting the Mining Industry, Civil, Rail, Agricultural and Workshop Testing And Tagging. My auto electrical service ranges from fault finding to new vehicle and mine compliance fit outs. I have a very strong focus on quality workmanship. I will upload the logo I have designed and want to use I am happy for the logo colour to change but the design itself must stay the same. I want the design to have a modern, eye catching, energetic feel. As I am a passionate motorsport fan I am happy for this to also influence the design. I am happy for the front of the card to have only the emblem and logo design and the back to have all the info.

Industry/Entity Type

Electrical

Contact Information for Business Card

MAE Marlow Auto Electrical, Dale Penrick, Auto Electrician, Mobile No 0417263859

Requirements
Must have
• On the business card it is mandatory that the following license numbers are shown:

MVRL38462
VDA L071348
ABN 61 839 204 518

```html
<!DOCTYPE html>
<html lang="en">
<head>
<meta charset="utf-8">
<title>Dale Penrick – Auto Electrician</title>
<link rel="stylesheet" href="https://fonts.googleapis.com/css2?family=Libre+Baskerville:wght@400;700&family=Jost:wght@400;500&display=swap">
<style>
  :root {
    --card-bg: #ffffff;
    --ink: #111111;
    --muted-ink: #555555;
    --accent-red: #e8141b;
    --flag-band: #d2d0d0;
  }
  html, body {
    margin: 0;
    padding: 0;
    width: 1200px;
    height: 686px;
    overflow: hidden;
    background: var(--card-bg);
  }
  .card {
    position: relative;
    width: 1200px;
    height: 686px;
    background: var(--card-bg);
  }
  .flag-band {
    position: absolute;
    left: 0;
    width: 1200px;
    height: 66px;
    background: var(--flag-band);
  }
  .flag-band--top { top: 0; }
  .flag-band--bottom { bottom: 0; }

  .centred {
    position: absolute;
    left: 0;
    width: 1200px;
    margin: 0;
    text-align: center;
    color: var(--ink);
  }

  .brand {
    top: 140px;
    font-family: "Jost", "Futura", sans-serif;
    font-weight: 500;
    font-size: 22px;
    line-height: 30px;
    letter-spacing: 3px;
  }
  .brand__short { color: var(--accent-red); }

  .identity__name {
    top: 253px;
    font-family: "Libre Baskerville", "Times New Roman", serif;
    font-weight: 400;
    font-size: 49px;
    line-height: 60px;
    letter-spacing: 0.5px;
  }
  .identity__rule {
    position: absolute;
    top: 317px;
    left: 422px;
    width: 359px;
    height: 5px;
    background: var(--ink);
  }
  .identity__role {
    top: 322px;
    font-family: "Jost", "Futura", sans-serif;
    font-weight: 500;
    font-size: 39px;
    line-height: 50px;
  }

  .contact {
    top: 425px;
    font-family: "Jost", "Futura", sans-serif;
    font-weight: 500;
    font-size: 43px;
    line-height: 56px;
    letter-spacing: 1px;
  }
  .contact__label { color: var(--accent-red); }

  .licences {
    top: 540px;
    font-family: "Jost", "Futura", sans-serif;
    font-weight: 400;
    font-size: 19px;
    line-height: 26px;
    letter-spacing: 1px;
    color: var(--muted-ink);
  }
  .licences__item + .licences__item::before {
    content: "•";
    margin: 0 14px;
    color: var(--accent-red);
  }
</style>
</head>
<body>
  <main class="card">
    <div class="flag-band flag-band--top" role="img" aria-label="Grey and white checkered flag band"></div>

    <p class="centred brand"><span class="brand__short">MAE</span> · Marlow Auto Electrical</p>

    <h1 class="centred identity__name">DALE PENRICK</h1>
    <div class="identity__rule"></div>
    <p class="centred identity__role">Auto Electrician</p>

    <p class="centred contact">
      <span class="contact__label">Mobile:</span>
      <span class="contact__number">0417263859</span>
    </p>

    <p class="centred licences">
      <span class="licences__item">MVRL38462</span><span class="licences__item">VDA L071348</span><span class="licences__item">ABN 61 839 204 518</span>
    </p>

    <div class="flag-band flag-band--bottom" role="img" aria-label="Grey and white checkered flag band"></div>
  </main>
</body>
</html>
```